Salon website

Need a web design for a new blow dry and hair extension boutique in CT
would like the color scheme to be gray, white and tiffany blue
Create a web site with about 4 pages showing
1 about us page
1 blow dry services page
1 hair extension services page
1 contact us page
1 membership page
1 parties page

Industry/Entity Type

Boutique

Colors
86cfc6
cfeae6
33b7a4
aaaaaa
cbcbcb
ffffff

```html
<!DOCTYPE html>
<html lang="en">
<head>
<meta charset="utf-8">
<title>Aveline Boutique — Parties</title>
<link rel="stylesheet" href="https://fonts.googleapis.com/css2?family=Questrial&family=Cabin:wght@400&display=swap">
<style>
  :root {
    --tiffany: #80d8d0;
    --tiffany-deep: #33b7a4;
    --gray-band: #cbcbcb;
    --gray-text: #555555;
    --white: #ffffff;
    --photo-dark: #2a2a2a;
    --photo-light: #9a9a9a;
  }
  * { margin: 0; padding: 0; box-sizing: border-box; }
  html, body { width: 1200px; height: 825px; overflow: hidden; background: var(--white); }
  body { position: relative; font-family: "Questrial", sans-serif; }

  .brand {
    position: absolute; left: 0; top: 0; width: 179px; height: 113px;
    background: var(--tiffany);
    display: flex; align-items: center; justify-content: center; gap: 10px;
  }
  .brand-dot { width: 16px; height: 16px; border-radius: 50%; background: var(--gray-text); }
  .brand-name { color: var(--gray-text); font-size: 20px; letter-spacing: 3px; }

  .main-nav {
    position: absolute; left: 195px; top: 0; width: 870px; height: 113px;
    background: var(--tiffany);
  }
  .nav-item {
    position: absolute; top: 40px; color: var(--white);
    font-size: 21px; letter-spacing: 0.5px; text-decoration: none; white-space: nowrap;
  }
  .nav-item.current { color: var(--gray-text); }

  .content-band {
    position: absolute; left: 0; top: 154px; width: 1200px; height: 486px;
    background: var(--gray-band);
  }
  .page-title {
    position: absolute; left: 16px; top: 22px;
    color: var(--white); font-weight: 400; font-size: 28px; letter-spacing: 0.5px;
  }
  .packages { position: absolute; left: 76px; top: 74px; width: 772px; }
  .package { margin-bottom: 24px; }
  .package-name {
    font-family: "Cabin", sans-serif; font-weight: 400;
    color: var(--tiffany-deep); font-size: 19px; line-height: 24px; letter-spacing: 0.3px;
  }
  .package-text {
    font-family: "Cabin", sans-serif; color: var(--white);
    font-size: 18.5px; line-height: 24.6px; text-indent: 30px;
  }

  .photo-frame {
    position: absolute; left: 932px; top: 46px; width: 249px; height: 410px;
    background: var(--white); padding: 8px;
  }
  .photo {
    width: 100%; height: 100%;
    background: linear-gradient(180deg, var(--photo-light) 0%, #555 45%, var(--photo-dark) 100%);
  }

  .site-footer {
    position: absolute; left: 0; top: 688px; width: 1200px; height: 137px;
    background: var(--tiffany);
  }
  .footer-link {
    position: absolute; top: 75px; color: var(--white);
    font-size: 21px; letter-spacing: 0.5px; text-decoration: none;
  }
</style>
</head>
<body>
  <header>
    <div class="brand">
      <span class="brand-dot"></span>
      <span class="brand-name">AVELINE</span>
    </div>
    <nav class="main-nav">
      <a class="nav-item" style="left:30px" href="#">ABOUT US</a>
      <a class="nav-item" style="left:171px" href="#">BLOW DRY</a>
      <a class="nav-item" style="left:318px" href="#">HAIR EXTENSIONS</a>
      <a class="nav-item" style="left:530px" href="#">CONTACT US</a>
      <a class="nav-item" style="left:708px" href="#">MEMBERSHIPS</a>
    </nav>
    <a class="nav-item current" style="left:1092px" href="#">PARTIES</a>
  </header>

  <main class="content-band">
    <h1 class="page-title">PARTIES</h1>
    <section class="packages">
      <article class="package">
        <h2 class="package-name">LEVEL 1</h2>
        <p class="package-text">Donec nisl nisi, facilisis eu tortor blandit, commodo laoreet mi. Integer vulputate non orci non aliquam. Maecenas volutpat ante id venenatis auctor. Nam dignissim blandit diam at volutpat. Suspendisse tempor nec arcu tempus cursus. Maecenas lobortis a mi sed faucibus.</p>
      </article>
      <article class="package">
        <h2 class="package-name">LEVEL 2</h2>
        <p class="package-text">Vivamus fringilla mauris in porta tempus. Aenean condimentum, lectus ut vulputate tempus, tortor turpis placerat neque, sit amet consectetur quam tortor pharetra enim. Ut faucibus orci non hendrerit vulputate. Nam gravida euismod ipsum, quis convallis massa molestie vel.</p>
      </article>
      <article class="package">
        <h2 class="package-name">LEVEL 3</h2>
        <p class="package-text">Sed aliquet quam vel fermentum scelerisque. Cras id placerat dolor. Integer quis euismod turpis.</p>
      </article>
    </section>
    <figure class="photo-frame">
      <div class="photo" role="img" aria-label="Black and white photo of two women reading magazines under salon hood dryers"></div>
    </figure>
  </main>

  <footer class="site-footer">
    <a class="footer-link" style="left:377px" href="#">© 2014 AVELINE BOUTIQUE</a>
    <a class="footer-link" style="left:660px" href="#">PRIVACY POLICY</a>
  </footer>
</body>
</html>
```